Corveth Thermal Job Add

We need a flashy ad we can post around our marketplace to attract new talent and employee. Our website has our company theme https://corveththermal.ca/

Target Market(s)

HVAC, Refrigeration, Trades

Industry/Entity Type

Trades

Requirements
Must have
• a few key phrases such as "Paying above industry standard" and "No on-call requirements"

```html
<!DOCTYPE html>
<html lang="en">
<head>
<meta charset="UTF-8">
<title>Corveth Thermal – We Are Hiring</title>
<link rel="stylesheet" href="https://fonts.googleapis.com/css2?family=Orbitron:wght@900&family=Roboto:wght@400&family=Montserrat:wght@300&family=Anton&display=swap">
<style>
  :root {
    --navy: #1a2c6c;
    --navy-deep: #132259;
    --navy-light: #25397d;
    --band-dark: #1d4f9a;
    --band-light: #6ea3dc;
    --orange: #f05a24;
    --orange-light: #f99a72;
    --icon-blue: #1b6fd1;
    --brand-blue: #1565c0;
    --white: #ffffff;
    --frame-grey: #9a9a9a;
    --ink: #111111;
  }
  * { margin: 0; padding: 0; box-sizing: border-box; }
  html, body { width: 1200px; height: 1200px; overflow: hidden; background: var(--navy); }
  .ad { position: relative; width: 1200px; height: 1200px; overflow: hidden; }

  .plant-backdrop {
    position: absolute; inset: 0;
    background:
      radial-gradient(ellipse at 70% 40%, var(--navy-light) 0%, transparent 60%),
      linear-gradient(160deg, var(--navy-light) 0%, var(--navy) 45%, var(--navy-deep) 100%);
  }
  .edge-band {
    position: absolute; left: 0; width: 1200px; height: 11px;
    background: linear-gradient(90deg, var(--band-dark) 0%, var(--band-light) 50%, var(--band-dark) 100%);
  }
  .edge-band.top { top: 0; }
  .edge-band.bottom { bottom: 0; }

  .brand-panel { position: absolute; left: 0; top: 29px; width: 507px; height: 260px; }
  .brand {
    position: absolute; left: 58px; top: 78px; width: 240px;
    display: flex; flex-direction: column; align-items: center;
  }
  .brand-dot { width: 70px; height: 70px; border-radius: 50%; background: var(--orange); margin-bottom: 14px; }
  .brand-name {
    font-family: 'Orbitron', sans-serif; font-weight: 900; color: var(--brand-blue);
    font-size: 27px; line-height: 1.1; text-align: center; letter-spacing: 0.5px;
  }

  .hero-gear { position: absolute; left: -30px; top: 390px; }
  .worker-photo {
    position: absolute; left: 28px; top: 250px; width: 440px; height: 937px;
    border-radius: 160px 160px 0 0;
    background: linear-gradient(180deg, #7a8a5e 0%, #6f7f55 40%, #c9a43a 70%, #6f7f55 100%);
  }

  .headline { position: absolute; right: 74px; text-align: right; font-family: 'Orbitron', sans-serif; font-weight: 900; }
  .headline.we-are { top: 122px; font-size: 84px; color: var(--white); letter-spacing: 2px; }
  .headline.hiring { top: 232px; font-size: 116px; color: var(--orange); font-style: normal; letter-spacing: 1px; }

  .perk { position: absolute; top: 432px; width: 240px; text-align: center; }
  .perk.pay { left: 624px; }
  .perk.on-call { left: 908px; }
  .perk svg { display: block; margin: 0 auto; }
  .perk-label {
    margin-top: 20px; font-family: 'Roboto', sans-serif; font-size: 29px; line-height: 39px; color: var(--white);
  }

  .join-line {
    position: absolute; right: 76px; top: 800px;
    font-family: 'Montserrat', sans-serif; font-weight: 300; font-size: 49px; color: var(--white); letter-spacing: 1px;
  }

  .apply-button {
    position: absolute; left: 691px; top: 895px; width: 434px; height: 148px;
    background: linear-gradient(180deg, #c9c9c9, var(--frame-grey)); border-radius: 6px; padding: 11px 12px;
  }
  .apply-face {
    width: 100%; height: 100%; border-radius: 4px;
    background: linear-gradient(180deg, var(--orange-light) 0%, var(--orange) 55%, #e8521c 100%);
    display: flex; align-items: center; justify-content: center;
    font-family: 'Anton', sans-serif; font-size: 76px; color: var(--ink); letter-spacing: 1px;
  }

  .contact { position: absolute; left: 565px; top: 1056px; display: flex; align-items: center; }
  .contact-number {
    margin-left: 42px; font-family: 'Roboto', sans-serif; font-size: 68px; color: var(--white); letter-spacing: 0.5px;
  }
</style>
</head>
<body>
<main class="ad">
  <div class="plant-backdrop" role="img" aria-label="Blue-tinted industrial mechanical plant room with pipes and equipment"></div>
  <div class="edge-band top"></div>
  <div class="edge-band bottom"></div>

  <svg class="brand-panel" width="507" height="260" viewBox="0 0 507 260">
    <polygon points="0,0 507,0 321,260 0,260" fill="#ffffff" opacity="0.96"/>
  </svg>
  <div class="brand">
    <div class="brand-dot"></div>
    <div class="brand-name">CORVETH<br>THERMAL</div>
  </div>

  <svg class="hero-gear" width="540" height="540" viewBox="0 0 540 540">
    <circle cx="270" cy="270" r="245" fill="none" stroke="#ffffff" stroke-width="44" stroke-dasharray="60 68.3"/>
    <circle cx="270" cy="270" r="200" fill="none" stroke="#ffffff" stroke-width="52"/>
  </svg>
  <div class="worker-photo" role="img" aria-label="Smiling bearded tradesman in green coveralls and a yellow tool belt, gesturing toward the offer"></div>

  <div class="headline we-are">WE ARE</div>
  <div class="headline hiring">HIRING!</div>

  <div class="perk pay">
    <svg width="180" height="180" viewBox="0 0 180 180" aria-hidden="true">
      <circle cx="90" cy="90" r="72" fill="#ffffff"/>
      <circle cx="90" cy="90" r="80" fill="none" stroke="#ffffff" stroke-width="18" stroke-dasharray="26 29.85"/>
      <g fill="var(--icon-blue)">
        <rect x="52" y="48" width="10" height="26"/>
        <path d="M64 50 h26 l10 8 h-18 z"/>
        <rect x="80" y="58" width="50" height="28" rx="3"/>
        <circle cx="105" cy="72" r="7" fill="#ffffff"/>
        <rect x="118" y="100" width="10" height="26"/>
        <path d="M62 102 q10 16 30 18 l24 0 l0 -14 l-22 0 q-16 0 -32 -4 z"/>
      </g>
    </svg>
    <div class="perk-label">Paying above<br>industry<br>standard</div>
  </div>

  <div class="perk on-call">
    <svg width="180" height="180" viewBox="0 0 180 180" aria-hidden="true">
      <circle cx="90" cy="90" r="72" fill="#ffffff"/>
      <circle cx="90" cy="90" r="80" fill="none" stroke="#ffffff" stroke-width="18" stroke-dasharray="26 29.85"/>
      <g fill="var(--icon-blue)">
        <rect x="92" y="46" width="46" height="36" rx="5"/>
        <path d="M100 82 l0 12 l12 -12 z"/>
        <rect x="101" y="56" width="26" height="4" fill="#ffffff"/>
        <rect x="101" y="66" width="18" height="4" fill="#ffffff"/>
        <path d="M52 76 q-4 30 24 54 q22 18 40 12 l6 -12 l-18 -14 l-10 8 q-16 -8 -26 -28 l8 -10 l-12 -18 z"/>
      </g>
    </svg>
    <div class="perk-label">No on-call<br>requirements</div>
  </div>

  <div class="join-line">JOIN OUR TEAM</div>

  <div class="apply-button"><div class="apply-face">APPLY NOW</div></div>

  <div class="contact">
    <svg width="84" height="84" viewBox="0 0 84 84" aria-hidden="true">
      <circle cx="42" cy="42" r="33" fill="var(--orange)"/>
      <circle cx="42" cy="42" r="36" fill="none" stroke="var(--orange)" stroke-width="12" stroke-dasharray="10 12.6"/>
      <path d="M30 28 q-4 16 10 28 q12 9 20 4 l2 -6 l-9 -7 l-5 4 q-8 -4 -12 -13 l4 -5 l-6 -8 z" fill="#ffffff"/>
    </svg>
    <div class="contact-number">(403) 555-0187</div>
  </div>
</main>
</body>
</html>
```